Regionale Imkerei sucht Etiketten-Design
Sehr gutes Endergebnis. Hochprofessionelle Abwicklung. Hat jeden Änderungswunsch zügig umgesetzt. Sehr angenehme, zielorientierte Kommunikation. Wirklich zu empfehlen, gerne wieder!
Zielgruppe
Mein Vater und ich haben eine regionale Hobbyimkerei, die wir nach und nach ausbauen wollen. Seit 1949 imkert unsere Familie. Ich bin in dritter Generation eingestiegen und möchte neben meinem know-how den Verkauf und das Marketing voran treiben um mit der Imkerei einen Nebenerwerb zu schaffen. Unsere Zielgruppe sind bewusste Verbraucher/innen, die gerne regional, hochqualitativ und nachhaltig einkaufen. Die meisten Honiggläser verkaufen wir direkt an der Haustür. Bis jetzt sind nur zwei Läden beliefert. Das soll sich dank musterwerkstatt ändern.
Aufgabenstellung
Ich habe eine Ausschreibung im PDF Format verfasst und beigefügt.
Was dort fehlt sind die Lagerungshinweise: kühl, trocken und dunkel lagern.
Für weitere Rückfragen gerne melden.

```html
<!DOCTYPE html>
<html lang="de">
<head>
<meta charset="utf-8">
<title>Tannenfrost – Honigetiketten</title>
<link href="https://fonts.googleapis.com/css2?family=Montserrat:wght@400;500;600;700&family=Great+Vibes&display=swap" rel="stylesheet">
<style>
  :root {
    --gold: #b8924a;
    --gold-light: #d9c49a;
    --pink: #d1077b;
    --orange: #f08a00;
    --green: #8cc043;
    --paper: #ffffff;
    --line: #ececec;
    --caption: #9a9a9a;
  }
  * { box-sizing: border-box; margin: 0; padding: 0; }
  html, body { width: 807px; height: 1200px; overflow: hidden; background: var(--paper); }
  body { position: relative; font-family: "Montserrat", sans-serif; color: var(--gold); }

  .swatches { position: absolute; top: 27px; left: 710px; display: flex; gap: 10px; }
  .swatches span { width: 17px; height: 17px; display: block; }

  .seal { position: absolute; filter: drop-shadow(0 1px 4px rgba(0,0,0,.12)); }
  .seal svg { display: block; width: 100%; height: 100%; }
  .seal .ring { font-family: "Montserrat", sans-serif; font-size: 9px; font-weight: 500; fill: var(--gold); letter-spacing: 1px; }
  .seal .brand { font-family: "Montserrat", sans-serif; font-size: 11px; font-weight: 500; fill: var(--gold); letter-spacing: 2px; }
  .seal .kind { font-family: "Montserrat", sans-serif; font-size: 21px; font-weight: 700; }
  .seal .note { font-family: "Montserrat", sans-serif; font-size: 17px; font-weight: 600; }

  .annotation { position: absolute; left: 520px; top: 189px; width: 140px; text-align: center;
    font-size: 9px; letter-spacing: 1.6px; color: #8a8a8a; line-height: 13px; }
  .annotation-arrow { position: absolute; left: 494px; top: 138px; }

  .strip { position: absolute; display: flex; align-items: center; justify-content: center;
    color: #fff; font-weight: 700; writing-mode: vertical-rl; transform: rotate(180deg); text-align: left; }

  .label { position: absolute; left: 101px; width: 605px; height: 148px; background: var(--paper);
    border: 1px solid var(--line); display: flex; }
  .label .panel-side { width: 196px; padding: 13px 10px 0; text-align: center; font-size: 7.6px; line-height: 9.5px; color: var(--gold); }
  .label .panel-side h3 { font-size: 7.8px; font-weight: 700; margin-bottom: 9px; }
  .label .panel-side strong { font-weight: 700; }
  .label .rule { width: 110px; height: 1px; background: var(--gold-light); margin: 9px auto 10px; }
  .label .weight { font-size: 14px; font-weight: 700; margin: 5px 0 5px; }
  .label .date-box { width: 101px; height: 23px; border: 1px solid var(--gold); margin: 4px auto 0; }
  .label .muted { margin-bottom: 4px; }

  .front { --s: 1; width: calc(214px * var(--s)); background: var(--paper); text-align: center; color: var(--gold);
    padding-top: calc(30px * var(--s)); }
  .front .name { font-size: calc(17px * var(--s)); font-weight: 500; letter-spacing: calc(1px * var(--s)); line-height: 1; }
  .front .sub { font-size: calc(5.8px * var(--s)); letter-spacing: calc(1.2px * var(--s)); font-weight: 500;
    margin-top: calc(6px * var(--s)); padding-top: calc(4px * var(--s)); border-top: 1px solid var(--gold-light);
    display: inline-block; }
  .front .script { font-family: "Great Vibes", cursive; font-size: calc(38px * var(--s)); line-height: 1; margin-top: calc(2px * var(--s)); }
  .front .tag { font-size: calc(7.8px * var(--s)); margin-top: calc(-3px * var(--s)); }
  .front .url { font-size: calc(7.8px * var(--s)); font-weight: 700; letter-spacing: calc(.5px * var(--s)); margin-top: calc(9px * var(--s)); }

  .front-card { position: absolute; top: 717px; height: 103px; border: 1px solid var(--line); }
  .front-card .front { --s: .7; width: 100%; padding-top: 16px; }

  .caption { position: absolute; top: 1137px; left: 0; width: 807px; text-align: center;
    font-size: 7.2px; letter-spacing: 1.3px; color: var(--caption); }
</style>
</head>
<body>

<div class="swatches"><span style="background:var(--orange)"></span><span style="background:var(--pink)"></span><span style="background:var(--green)"></span></div>

<!-- Hauptsiegel -->
<div class="seal" style="left:327px;top:67px;width:152px;height:152px;">
  <svg viewBox="-100 -100 200 200">
    <defs><path id="ring-a" d="M -84,0 A 84 84 0 1 1 84 0 A 84 84 0 1 1 -84 0"/></defs>
    <circle r="100" fill="#fff"/>
    <text class="ring"><textPath href="#ring-a" textLength="520" lengthAdjust="spacing">WWW.TANNENFROST.DE · TANNENFROST · E. KORNHUBER · LINDENAUER STR. 14 · 75100 WALDTAL ·</textPath></text>
    <text class="brand" x="0" y="-30" text-anchor="middle">TANNENFROST</text>
    <text class="kind" x="0" y="10" text-anchor="middle" fill="var(--pink)">Blütenhonig</text>
    <text class="note" x="0" y="30" text-anchor="middle" fill="var(--pink)">mit Linde und</text>
    <text class="note" x="0" y="50" text-anchor="middle" fill="var(--pink)">Himbeere</text>
  </svg>
</div>

<svg class="annotation-arrow" width="80" height="34" viewBox="0 0 80 34">
  <path d="M76 32 C60 14 34 8 4 9" fill="none" stroke="#555" stroke-width="1"/>
  <path d="M10 4 L3 9 L10 13" fill="none" stroke="#555" stroke-width="1"/>
</svg>
<div class="annotation">QUALITÄTSSIEGEL<br>56 MM DURCHMESSER</div>

<div class="strip" style="left:384px;top:217px;width:40px;height:89px;background:var(--pink);font-size:7.5px;line-height:9px;">Blütenhonig<br>Cremig &amp; weich</div>

<!-- Rundumetikett oben -->
<div class="label" style="top:306px;">
  <div class="panel-side">
    <h3>Bienenhonig aus der Region</h3>
    <p>Honig ist ein reines Naturprodukt ohne Zusätze. Diese Reinheit und Natürlichkeit sind in <strong>Tannenfrost</strong>-Honig vereint. Geniessen Sie goldene Momente mit ökologischem Natur-Honig aus eigener Ernte und regionalem Ursprung.</p>
    <div class="rule"></div>
    <p>Tannenfrost · E. Kornhuber<br>Lindenauer Str. 14 · 75100 Waldtal<br><strong>www.tannenfrost.de</strong></p>
  </div>
  <div class="front">
    <div class="name">TANNENFROST</div>
    <div class="sub">HONIG AUS DEUTSCHLAND</div>
    <div class="script">Bienenhonig</div>
    <div class="tag">Für goldene Momente</div>
    <div class="url">WWW.TANNENFROST.DE</div>
  </div>
  <div class="panel-side">
    <h3>100% Honig aus Deutschland</h3>
    <p>Mehrwegglas</p>
    <div class="weight">400 g ℮</div>
    <p class="muted">Trocken, dunkel und vor Wärme<br>geschützt lagern.</p>
    <p style="margin-top:9px;">Mindestens haltbar bis / Los-Nr.:</p>
    <div class="date-box"></div>
  </div>
</div>

<!-- Sortenreihe -->
<div class="seal" style="left:144px;top:554px;width:106px;height:106px;">
  <svg viewBox="-100 -100 200 200">
    <defs><path id="ring-b" d="M -84,0 A 84 84 0 1 1 84 0 A 84 84 0 1 1 -84 0"/></defs>
    <circle r="100" fill="#fff"/>
    <text class="ring"><textPath href="#ring-b" textLength="520" lengthAdjust="spacing">WWW.TANNENFROST.DE · TANNENFROST · E. KORNHUBER · LINDENAUER STR. 14 · 75100 WALDTAL ·</textPath></text>
    <text class="brand" x="0" y="-30" text-anchor="middle">TANNENFROST</text>
    <text class="kind" x="0" y="10" text-anchor="middle" fill="var(--orange)">Blütenhonig</text>
    <text class="note" x="0" y="30" text-anchor="middle" fill="var(--orange)">Cremig und</text>
    <text class="note" x="0" y="50" text-anchor="middle" fill="var(--orange)">weich</text>
  </svg>
</div>
<div class="seal" style="left:351px;top:554px;width:106px;height:106px;">
  <svg viewBox="-100 -100 200 200">
    <defs><path id="ring-c" d="M -84,0 A 84 84 0 1 1 84 0 A 84 84 0 1 1 -84 0"/></defs>
    <circle r="100" fill="#fff"/>
    <text class="ring"><textPath href="#ring-c" textLength="520" lengthAdjust="spacing">WWW.TANNENFROST.DE · TANNENFROST · E. KORNHUBER · LINDENAUER STR. 14 · 75100 WALDTAL ·</textPath></text>
    <text class="brand" x="0" y="-30" text-anchor="middle">TANNENFROST</text>
    <text class="kind" x="0" y="10" text-anchor="middle" fill="var(--pink)">Blütenhonig</text>
    <text class="note" x="0" y="30" text-anchor="middle" fill="var(--pink)">mit Linde und</text>
    <text class="note" x="0" y="50" text-anchor="middle" fill="var(--pink)">Himbeere</text>
  </svg>
</div>
<div class="seal" style="left:559px;top:554px;width:106px;height:106px;">
  <svg viewBox="-100 -100 200 200">
    <defs><path id="ring-d" d="M -84,0 A 84 84 0 1 1 84 0 A 84 84 0 1 1 -84 0"/></defs>
    <circle r="100" fill="#fff"/>
    <text class="ring"><textPath href="#ring-d" textLength="520" lengthAdjust="spacing">WWW.TANNENFROST.DE · TANNENFROST · E. KORNHUBER · LINDENAUER STR. 14 · 75100 WALDTAL ·</textPath></text>
    <text class="brand" x="0" y="-30" text-anchor="middle">TANNENFROST</text>
    <text class="kind" x="0" y="10" text-anchor="middle" fill="var(--green)">Waldhonig</text>
    <text class="note" x="0" y="30" text-anchor="middle" fill="var(--green)">Kräftig und</text>
    <text class="note" x="0" y="50" text-anchor="middle" fill="var(--green)">herzhaft</text>
  </svg>
</div>

<div class="strip" style="left:183px;top:659px;width:29px;height:60px;background:var(--orange);font-size:5px;line-height:6.5px;">Blütenhonig<br>Cremig &amp; weich</div>
<div class="strip" style="left:390px;top:659px;width:29px;height:60px;background:var(--pink);font-size:5px;line-height:6.5px;">Blütenhonig mit<br>Linde &amp; Himbeere</div>
<div class="strip" style="left:598px;top:659px;width:29px;height:60px;background:var(--green);font-size:5px;line-height:6.5px;">Waldhonig<br>Kräftig &amp; herzhaft</div>

<div class="front-card" style="left:122px;width:150px;">
  <div class="front"><div class="name">TANNENFROST</div><div class="sub">HONIG AUS DEUTSCHLAND</div><div class="script">Bienenhonig</div><div class="tag">Für goldene Momente</div><div class="url">WWW.TANNENFROST.DE</div></div>
</div>
<div class="front-card" style="left:329px;width:150px;">
  <div class="front"><div class="name">TANNENFROST</div><div class="sub">HONIG AUS DEUTSCHLAND</div><div class="script">Bienenhonig</div><div class="tag">Für goldene Momente</div><div class="url">WWW.TANNENFROST.DE</div></div>
</div>
<div class="front-card" style="left:537px;width:150px;">
  <div class="front"><div class="name">TANNENFROST</div><div class="sub">HONIG AUS DEUTSCHLAND</div><div class="script">Bienenhonig</div><div class="tag">Für goldene Momente</div><div class="url">WWW.TANNENFROST.DE</div></div>
</div>

<!-- Rundumetikett flach -->
<div class="label" style="top:932px;">
  <div class="panel-side">
    <h3>Bienenhonig aus der Region</h3>
    <p>Honig ist ein reines Naturprodukt ohne Zusätze. Diese Reinheit und Natürlichkeit sind in <strong>Tannenfrost</strong>-Honig vereint. Geniessen Sie goldene Momente mit ökologischem Natur-Honig aus eigener Ernte und regionalem Ursprung.</p>
    <div class="rule"></div>
    <p>Tannenfrost · E. Kornhuber<br>Lindenauer Str. 14 · 75100 Waldtal<br><strong>www.tannenfrost.de</strong></p>
  </div>
  <div class="front">
    <div class="name">TANNENFROST</div>
    <div class="sub">HONIG AUS DEUTSCHLAND</div>
    <div class="script">Bienenhonig</div>
    <div class="tag">Für goldene Momente</div>
    <div class="url">WWW.TANNENFROST.DE</div>
  </div>
  <div class="panel-side">
    <h3>100% Honig aus Deutschland</h3>
    <p>Mehrwegglas</p>
    <div class="weight">400 g ℮</div>
    <p class="muted">Trocken, dunkel und vor Wärme<br>geschützt lagern.</p>
    <p style="margin-top:9px;">Mindestens haltbar bis / Los-Nr.:</p>
    <div class="date-box"></div>
  </div>
</div>

<div class="caption">ETIKETTEN „TANNENFROST“ ABMESSUNG 180 X 44 MM · WWW.TANNENFROST.DE</div>

</body>
</html>
```